Startup Drone Platform Company business card

We are needing a business card design for our employees. We are a startup drone platform. We are looking for a business card that has our logo on one side, with the employee/company details on the opposite side. We are looking for something that is very eye catching, modern, and bold.

Target Market(s)

This will target both drone pilots and drone businesses, along with all the industries that could utilize drone services (aerial video, aerial photos, inspections, 3d mapping, etc).

Industry/Entity Type

Business

```html
<!DOCTYPE html>
<html lang="en">
<head>
<meta charset="UTF-8">
<title>Aerolane Hire — Business Card</title>
<link href="https://fonts.googleapis.com/css2?family=Source+Sans+3:wght@400;600&display=swap" rel="stylesheet">
<style>
  :root {
    --backdrop: #ece9e4;
    --kraft-light: #d2b288;
    --kraft-mid: #c6a277;
    --kraft-dark: #b8936a;
    --ink: #15120e;
    --card-shadow: rgba(60, 40, 20, 0.22);
  }
  * { margin: 0; padding: 0; box-sizing: border-box; }
  html, body {
    width: 1200px;
    height: 900px;
    overflow: hidden;
    background: var(--backdrop);
    font-family: "Source Sans 3", "Myriad Pro", Arial, sans-serif;
    color: var(--ink);
  }
  .canvas {
    position: relative;
    width: 1200px;
    height: 900px;
  }
  .card {
    position: absolute;
    width: 556px;
    height: 342px;
    background: radial-gradient(ellipse at 45% 30%, var(--kraft-light) 0%, var(--kraft-mid) 55%, var(--kraft-dark) 100%);
    box-shadow: 0 6px 18px var(--card-shadow);
  }
  .card--details { left: 238px; top: 62px; }
  .card--brand { left: 458px; top: 518px; width: 560px; }

  .details {
    position: absolute;
    left: 0; right: 0; top: 68px;
    text-align: center;
  }
  .details__name {
    font-size: 19px;
    font-weight: 600;
    letter-spacing: 0.01em;
    line-height: 24px;
  }
  .details__role {
    font-size: 15px;
    line-height: 20px;
  }
  .details__rule {
    width: 165px;
    height: 1px;
    background: var(--ink);
    margin: 18px auto 26px;
  }
  .details__contact,
  .details__address {
    font-size: 15px;
    line-height: 19px;
  }
  .details__address { margin-top: 19px; }

  .brand {
    position: absolute;
    left: 0; right: 0; top: 0; bottom: 0;
    display: flex;
    align-items: center;
    justify-content: center;
    gap: 18px;
    padding-top: 4px;
  }
  .brand__dot {
    width: 18px;
    height: 18px;
    border-radius: 50%;
    background: var(--ink);
  }
  .brand__name {
    font-size: 27px;
    font-weight: 400;
    letter-spacing: 0.52em;
    margin-right: -0.52em;
  }
</style>
</head>
<body>
  <main class="canvas">
    <section class="card card--details">
      <div class="details">
        <p class="details__name">MARCUS ELLERY</p>
        <p class="details__role">Managing Director</p>
        <div class="details__rule"></div>
        <p class="details__contact">044-382-6150</p>
        <p class="details__contact">hello@aerolanehire.com</p>
        <p class="details__contact">www.aerolanehire.com</p>
        <p class="details__address">58 Harbour View Road</p>
        <p class="details__address details__address--line2" style="margin-top:0">Northfield, AB | 204517</p>
      </div>
    </section>

    <section class="card card--brand">
      <div class="brand">
        <span class="brand__dot"></span>
        <span class="brand__name">AEROLANE HIRE</span>
      </div>
    </section>
  </main>
</body>
</html>
```